Business Cards for an engineering & contracting company
Korvane Group
Business Cards for an engineering & contracting company - Architecture
Creative Brief
Professional
Architect Marwan Tarek Korvane
CEO - Project Manager
Chiyah, Blvd Rue Doumani, Next to Meridel Plaza, Korvane Tower, Blk B - 2nd floor
marwan@korvanegroup-example.com
www.korvanegroup-example.com
the word "Architect" can be written in a nice design before the name, The name is "Marwan Tarek Korvane". The company name is "Korvane Group" The country is " Beirut, Lebanon" Its preferable is the card is made of 2 or 3 colors that make it impressive
A design that is related to the company description, which is (architecture, engineering, design, contracting and construction) The logo may be a solution if its alone or with something else added to it.
Korvane Korvane
I'd like to see other stationery designs too in addition to the business card.

```html
<!DOCTYPE html>
<html lang="en">
<head>
<meta charset="utf-8">
<title>Korvane Group – Business Cards</title>
<link href="https://fonts.googleapis.com/css2?family=Open+Sans:wght@400;600;700&display=swap" rel="stylesheet">
<style>
  :root{
    --bg:#c8c9cb;
    --brand-blue:#1a6ef2;
    --deep-blue:#1f5fc4;
    --card-white:#fbfbfb;
    --text-grey:#6a6d72;
    --logo-grey:#8b8f94;
  }
  *{margin:0;padding:0;box-sizing:border-box}
  html,body{width:1200px;height:902px;overflow:hidden}
  body{background:var(--bg);font-family:"Open Sans",Arial,sans-serif;position:relative}
  .card{position:absolute;width:600px;height:343px;box-shadow:0 6px 18px rgba(0,0,0,.18)}
  .card-back{left:150px;top:80px;background:var(--brand-blue);display:flex;align-items:center;justify-content:center}
  .card-back .web{color:#fff;font-size:22px;letter-spacing:2px;font-weight:400}
  .card-front{left:450px;top:470px;background:var(--card-white)}
  .person{position:absolute;right:44px;top:40px;text-align:right}
  .person .name{color:var(--deep-blue);font-weight:700;font-size:22px;line-height:30px}
  .person .role{color:var(--text-grey);font-size:17px;line-height:26px}
  .logo{position:absolute;left:44px;top:118px;display:flex;align-items:center;gap:10px}
  .logo .mark{width:22px;height:22px;background:var(--brand-blue)}
  .logo .wordmark{color:var(--logo-grey);font-size:25px;font-weight:600;letter-spacing:1px;line-height:34px}
  .front-web{position:absolute;right:44px;top:170px;color:var(--deep-blue);font-size:14px;letter-spacing:1.5px;font-weight:600}
  .contacts{position:absolute;left:44px;right:44px;bottom:26px;list-style:none;color:var(--text-grey);font-size:12px;line-height:18px}
  .contacts li{display:flex;align-items:flex-start;gap:8px;margin-top:4px}
  .contacts svg{flex:0 0 11px;width:11px;height:11px;margin-top:4px;fill:var(--brand-blue)}
</style>
</head>
<body>
  <section class="card card-back">
    <p class="web">www.korvanegroup-example.com</p>
  </section>

  <section class="card card-front">
    <div class="person">
      <p class="name">Marwan Tarek Korvane</p>
      <p class="role">CEO - Project Manager</p>
    </div>
    <div class="logo">
      <span class="mark"></span>
      <span class="wordmark">KORVANE GROUP</span>
    </div>
    <p class="front-web">www.korvanegroup-example.com</p>
    <ul class="contacts">
      <li><svg viewBox="0 0 10 10"><path d="M2 0h2l1 3-1.3 1a6 6 0 0 0 2.3 2.3L7 5l3 1v2c0 1-1 2-2 2A8 8 0 0 1 0 2c0-1 1-2 2-2z"/></svg><span>01 555 014</span></li>
      <li><svg viewBox="0 0 10 10"><rect x="0" y="2" width="10" height="6"/></svg><span>marwan@korvanegroup-example.com</span></li>
      <li><svg viewBox="0 0 10 10"><path d="M5 0a3.5 3.5 0 0 1 3.5 3.5C8.5 6 5 10 5 10S1.5 6 1.5 3.5A3.5 3.5 0 0 1 5 0z"/></svg><span>Chiyah, Blvd Rue Doumani, Next to Meridel Plaza,<br>Korvane Tower, Blk B - 2nd floor</span></li>
    </ul>
  </section>
</body>
</html>
```